Digital Teaching Model

The primary goal would be to develop a new vision for the Digital Teaching Powerpt. I am attaching an older version called DT, I would like it updated to include our colors and our models with new images that make the presentation more relevant. I am also attaching brochures around the new curriculum. The Links below will give examples to the digital lessons: https://512.brevinotal.com/review/content/7c3d9a41-58b2-4f07-b6e1-2a9d0c4f8e17/review and https://512.brevinotal.com/review/content/4e81b6f2-0d93-47a5-8c2e-9f1a73d5b06c/review. the Digital teaching PWRPT should include some of these images and the color palet from the company brochure which is attached.
Education

```html
<!DOCTYPE html>
<html lang="en">
<head>
<meta charset="utf-8">
<title>Digital Teaching Model — Slide Deck</title>
<link href="https://fonts.googleapis.com/css2?family=Arimo:wght@400;700&family=Montserrat:wght@600;700&display=swap" rel="stylesheet">
<style>
:root{
  --orange:#f07f1f;
  --orange-deep:#e36a12;
  --charcoal:#3a3a3c;
  --ink:#333333;
  --grey:#8a8a8a;
  --line:#b9b9b9;
  --paper:#ffffff;
  --canvas:#f2f2f2;
  --teal:#1f8a78;
  --blue:#2b7bbf;
  --purple:#8b3a9c;
  --photo-warm:linear-gradient(135deg,#c98a4e,#6b4a33);
  --photo-cool:linear-gradient(135deg,#8e8a86,#3f3a36);
}
*{box-sizing:border-box;margin:0;padding:0}
html,body{width:1200px;height:4630px;overflow:hidden}
body{background:var(--canvas);font-family:"Arimo",Arial,sans-serif;color:var(--ink);position:relative}
.slide{position:absolute;width:560px;height:314px;background:var(--paper);overflow:hidden;box-shadow:0 2px 8px rgba(0,0,0,.12)}
.slide.small{transform:scale(.64);transform-origin:top left}
.slide.hero{transform:scale(1.9);transform-origin:top left}
.slide svg.bg{position:absolute;inset:0;width:560px;height:314px}
.slide-title{position:absolute;top:24px;left:0;right:0;text-align:center;font-size:21px;font-weight:400;color:var(--ink);letter-spacing:-.2px;white-space:nowrap}
.slide-foot{position:absolute;left:14px;bottom:9px;font-size:6.5px;color:var(--grey);white-space:nowrap}
.slide-foot b{font-weight:400;margin-right:3px}
.mini-logo{position:absolute;right:14px;bottom:7px;display:flex;align-items:center;gap:3px;font-size:9px;color:var(--charcoal)}
.mini-logo i{width:7px;height:7px;background:var(--orange);display:block}
.brand{position:absolute;display:flex;align-items:center;gap:8px;white-space:nowrap}
.brand-mark{width:22px;height:22px;background:var(--orange);display:block;flex:none}
.brand-name{font-size:32px;color:var(--charcoal);font-weight:400;letter-spacing:-.5px}
.brand-tag{position:absolute;font-size:7px;letter-spacing:1px;color:var(--grey);white-space:nowrap}
.ph{position:absolute}
.ph.warm{background:var(--photo-warm)}
.ph.cool{background:var(--photo-cool)}
.ph.soft{background:linear-gradient(135deg,#d9d9d9,#a9a9a9)}
.cover-title{position:absolute;font-family:"Montserrat",Arial,sans-serif;font-weight:700;color:#fff;font-size:22px;line-height:1.12;letter-spacing:.3px}
.cover-sub{position:absolute;font-size:6px;letter-spacing:2px;color:#cfcfcf;white-space:nowrap}
.year-pill{position:absolute;font-size:7px;color:var(--ink);border:1px solid var(--line);border-radius:8px;padding:2px 8px}
.cover-word{position:absolute;font-size:14px;color:var(--orange);white-space:nowrap}
.locus-lines{position:absolute;inset:0;width:560px;height:314px}
.mode-tag{position:absolute;left:0;top:52px;width:120px;height:15px;background:var(--charcoal);color:var(--orange);font-size:8px;line-height:15px;padding-left:10px;clip-path:polygon(0 0,100% 0,88% 100%,0 100%)}
.node-label{position:absolute;background:var(--orange);color:#fff;font-size:7px;line-height:11px;padding:0 10px;border-radius:2px;transform:translateX(-50%)}
.ph-teacher{left:235px;top:78px;width:90px;height:38px}
.ph-curric{left:62px;top:132px;width:112px;height:58px}
.ph-tech{left:402px;top:138px;width:70px;height:54px}
.ph-student{left:238px;top:230px;width:82px;height:36px}
.era{position:absolute;top:108px;width:80px}
.era-head{height:16px;font-size:8px;color:#fff;text-align:center;line-height:16px;border-radius:3px 3px 0 0}
.era-head.o{background:var(--orange)}
.era-head.d{background:var(--charcoal)}
.era-shot{height:44px;border:2px solid var(--orange);border-top:0}
.era.dark .era-shot{border-color:var(--charcoal)}
.era-label{position:absolute;top:88px;width:100%;text-align:center;font-size:6.5px;color:var(--grey);line-height:1.2}
.loop-box{position:absolute;width:70px;height:50px;color:#fff;font-size:7px;text-align:center;display:flex;flex-direction:column;align-items:center;justify-content:flex-end;padding-bottom:6px;border-radius:3px;gap:5px}
.bx-orange{background:var(--orange)}
.bx-dark{background:var(--charcoal)}
.bx-teal{background:var(--teal)}
.bx-purple{background:var(--purple)}
.bx-blue{background:var(--blue)}
.bx-gold{background:#f3b23a;color:var(--ink)}
.bullets{position:absolute;list-style:none;font-size:8px;color:var(--ink)}
.bullets li{position:relative;padding-left:18px;margin-bottom:8px}
.bullets li::before{content:"";position:absolute;left:2px;top:0;width:0;height:0;border-left:5px solid transparent;border-right:5px solid transparent;border-bottom:9px solid var(--orange)}
.bullets li small{display:block;color:var(--orange);font-size:6.5px;margin-top:1px}
.band{position:absolute;left:40px;top:92px;width:380px;height:18px;background:#ececec;font-size:8px;line-height:18px;padding-left:14px}
.copy{position:absolute;left:40px;top:42px;width:210px;font-size:5.3px;line-height:1.45;color:#555;text-align:justify}
.scan{position:absolute;left:40px;top:62px;width:480px;border-collapse:collapse;font-size:5.6px;color:#555}
.scan th{font-weight:400;text-align:center;padding:3px 2px;border-bottom:1px solid var(--line)}
.scan th:first-child{text-align:left;width:170px}
.scan td{padding:2px 2px;height:11px;text-align:center;border-right:1px dotted #ddd}
.scan td:first-child{text-align:left}
.scan tr.gap td{height:6px}
.tick{display:inline-block;width:8px;height:8px;background:#fbe1c9;color:var(--orange);font-size:7px;line-height:8px}
</style>
</head>
<body>

<!-- ===== Overview collage ===== -->
<section class="slide small" style="left:30px;top:30px">
  <h2 class="slide-title" style="font-size:24px">Evolution of Digital Instructional Tools</h2>
  <svg class="bg" viewBox="0 0 560 314"><line x1="30" y1="182" x2="530" y2="182" stroke="#ccc" stroke-dasharray="2 3"/></svg>
  <div class="era" style="left:40px"><div class="era-head o">1985</div><div class="era-shot ph soft" style="position:relative" role="img" aria-label="Early computer lab"></div><div class="era-label">Computer Labs</div></div>
  <div class="era dark" style="left:140px"><div class="era-head d">2000</div><div class="era-shot ph soft" style="position:relative" role="img" aria-label="Electronic whiteboard"></div><div class="era-label">Electronic Whiteboards</div></div>
  <div class="era" style="left:240px"><div class="era-head o">2010</div><div class="era-shot ph soft" style="position:relative" role="img" aria-label="In-class computing"></div><div class="era-label">In-class Computing</div></div>
  <div class="era dark" style="left:340px"><div class="era-head d">2012</div><div class="era-shot ph soft" style="position:relative" role="img" aria-label="Print and digital materials"></div><div class="era-label">Print + Digital</div></div>
  <div class="era" style="left:440px"><div class="era-head o">Next Gen</div><div class="era-shot ph soft" style="position:relative" role="img" aria-label="Digital teaching platform classroom"></div><div class="era-label">Digital Teaching Platform</div></div>
  <p class="slide-foot"><b>6</b>| Kestrel™ Vantage Careers™ 2021 Trademark Kestrel LLC</p><span class="mini-logo"><i></i>Kestrel</span>
</section>

<section class="slide small" style="left:421px;top:30px">
  <h2 class="slide-title">Traditional LMS</h2>
  <div class="band">Skinnerian Teaching Machines—ILS's</div>
  <ul class="bullets" style="left:60px;top:126px">
    <li>"Teacher Proof" Technology</li><li>Closed Curriculum</li><li>Fixed Map from Assessment to Curriculum</li><li>Lab or Back of the Room</li><li>One student only</li>
  </ul>
  <div class="ph warm" style="left:400px;top:60px;width:130px;height:254px" role="img" aria-label="Student holding books"></div>
  <p class="slide-foot"><b>9</b>| Kestrel™ Vantage Careers™ 2021 Trademark Kestrel LLC</p><span class="mini-logo"><i></i>Kestrel</span>
</section>

<section class="slide small" style="left:812px;top:30px">
  <h2 class="slide-title">Traditional LMS Instructional Loop</h2>
  <svg class="bg" viewBox="0 0 560 314">
    <path d="M130 170 A60 60 0 0 1 190 110" fill="none" stroke="var(--orange)" stroke-width="24"/>
    <path d="M190 110 A60 60 0 1 1 130 170" fill="none" stroke="var(--charcoal)" stroke-width="24"/>
    <path d="M300 170 h24 l-6 -7 M324 170 l-6 7" stroke="#aaa" stroke-width="5" fill="none"/>
    <path d="M400 170 h24 l-6 -7 M424 170 l-6 7" stroke="#aaa" stroke-width="5" fill="none"/>
  </svg>
  <div class="loop-box bx-orange" style="left:60px;top:145px">Content Management</div>
  <div class="loop-box bx-dark" style="left:220px;top:145px">Assessment</div>
  <div class="loop-box bx-teal" style="left:330px;top:145px">Grade Book</div>
  <div class="loop-box bx-purple" style="left:430px;top:145px">SIS</div>
  <p class="slide-foot"><b>8</b>| Kestrel™ Vantage Careers™ 2021 Trademark Kestrel LLC</p><span class="mini-logo"><i></i>Kestrel</span>
</section>

<section class="slide small" style="left:30px;top:260px">
  <svg class="bg" viewBox="0 0 560 314"><polygon points="470,0 560,0 560,60" fill="var(--orange)"/><polygon points="500,0 560,0 560,28" fill="var(--charcoal)"/></svg>
  <p class="copy">The Digital Teaching Platform offers a full curriculum of guided learning sequences with applied activities, media presentations, practice exercises and short quizzes. Before class the teacher uses planning tools to prepare lessons, set goals and choose resources. During class students work alone, in pairs or in groups while the teacher watches progress in real time and adjusts instruction. After class the platform gathers results, builds reports and suggests next steps for every learner. In this way the classroom becomes a flexible space where each student is supported and every teacher stays in control.</p>
  <div class="ph" style="left:300px;top:40px;width:150px;height:230px;background:linear-gradient(135deg,#2e5fae,#17356f)" role="img" aria-label="Book cover on digital teaching platforms"></div>
  <p class="slide-foot"><b>7</b>| Kestrel™ Vantage Careers™ 2021 Trademark Kestrel LLC</p><span class="mini-logo"><i></i>Kestrel</span>
</section>

<section class="slide small" style="left:421px;top:260px">
  <h2 class="slide-title">Instructional Delivery Scan</h2>
  <table class="scan">
    <tr><th>21st Century School Environment</th><th>Course Platform LMS</th><th>Course Delivery LMS</th><th>Digital Teaching Platform</th><th>Text book</th><th>e-book</th></tr>
    <tr><td>Interactive Digital Environment</td><td><span class="tick">✓</span></td><td><span class="tick">✓</span></td><td><span class="tick">✓</span></td><td></td><td></td></tr>
    <tr><td>Virtual Courses</td><td></td><td><span class="tick">✓</span></td><td></td><td></td><td></td></tr>
    <tr><td>Teacher Administration Tools</td><td><span class="tick">✓</span></td><td><span class="tick">✓</span></td><td><span class="tick">✓</span></td><td></td><td></td></tr>
    <tr><td>Curriculum Content</td><td></td><td><span class="tick">✓</span></td><td><span class="tick">✓</span></td><td><span class="tick">✓</span></td><td><span class="tick">✓</span></td></tr>
  </table>
  <p class="slide-foot"><b>20</b>| Kestrel™ Vantage Careers™ 2021 Trademark Kestrel LLC</p><span class="mini-logo"><i></i>Kestrel</span>
</section>

<section class="slide small" style="left:812px;top:260px">
  <div class="brand" style="left:200px;top:132px"><span class="brand-mark"></span><span class="brand-name">Kestrel</span></div>
  <p class="brand-tag" style="left:222px;top:176px">LEARN • LEAD • GROW</p>
</section>

<section class="slide hero" style="left:68px;top:500px">
  <svg class="bg" viewBox="0 0 560 314">
    <path d="M300 0 H560 V198 C470 198 390 172 338 112 C312 80 302 40 300 0Z" fill="var(--charcoal)"/>
    <path d="M0 250 C170 250 300 250 420 228 C480 217 530 210 560 206 V198 C470 198 390 172 338 112 C312 80 302 40 300 0 H0Z" fill="var(--orange)"/>
  </svg>
  <div class="ph warm" style="left:0;top:0;width:330px;height:238px;clip-path:path('M0 0 H296 C298 44 310 86 334 118 C360 152 380 170 400 180 C300 228 160 232 0 236 Z')" role="img" aria-label="Graduation cap tassel close-up"></div>
  <h1 class="cover-title" style="left:395px;top:40px">DIGITAL<br>TEACHING<br>MODEL</h1>
  <p class="cover-sub" style="left:395px;top:124px">2021</p>
  <div class="brand" style="left:380px;top:236px"><span class="brand-mark" style="width:16px;height:16px"></span><span class="brand-name" style="font-size:24px">Kestrel</span></div>
  <p class="brand-tag" style="left:404px;top:266px;font-size:5px">LEARN • LEAD • GROW</p>
  <p class="slide-foot" style="font-size:5px">Kestrel™ Vantage Careers™ | 2021 Trademark Kestrel LLC</p>
</section>

<!-- ===== Row 1 ===== -->
<section class="slide" style="left:27px;top:1225px">
  <svg class="bg" viewBox="0 0 560 314">
    <path d="M0 0 H560 V150 C430 150 330 228 200 234 C120 238 60 222 0 208Z" fill="var(--charcoal)"/>
    <path d="M0 208 C60 222 120 238 200 234 C330 228 430 150 560 150 V172 C440 172 340 246 200 252 C110 256 50 242 0 232Z" fill="var(--orange)"/>
  </svg>
  <div class="ph warm" style="left:250px;top:0;width:310px;height:150px;clip-path:path('M0 0 H310 V150 C220 150 150 190 80 215 C60 140 30 60 0 0Z')" role="img" aria-label="Group of friends with arms around each other at sunset"></div>
  <h1 class="cover-title" style="left:40px;top:42px">DIGITAL<br>TEACHING<br>MODEL</h1>
  <p class="cover-sub" style="left:40px;top:130px">Subtitle Goes here</p>
  <div class="brand" style="left:40px;top:250px"><span class="brand-mark" style="width:18px;height:18px"></span><span class="brand-name" style="font-size:28px">Kestrel</span></div>
  <p class="brand-tag" style="left:66px;top:284px;font-size:5.5px">LEARN • LEAD • GROW</p>
  <span class="year-pill" style="right:18px;bottom:12px">2021</span>
</section>

<section class="slide" style="left:613px;top:1225px">
  <svg class="bg" viewBox="0 0 560 314">
    <polygon points="300,0 560,0 560,130" fill="var(--orange)"/>
    <polygon points="0,314 0,150 560,20 560,314" fill="#c86a1a"/>
  </svg>
  <div class="ph warm" style="left:0;top:0;width:560px;height:314px;clip-path:polygon(0 55%,100% 12%,100% 100%,0 100%)" role="img" aria-label="Hands framing a sunset"></div>
  <svg class="bg" viewBox="0 0 560 314"><polygon points="0,140 420,0 300,0 0,0" fill="var(--orange)" opacity=".9"/></svg>
  <div class="brand" style="left:24px;top:22px"><span class="brand-mark" style="width:9px;height:9px"></span><span class="brand-name" style="font-size:14px">Kestrel</span></div>
  <p class="cover-word" style="left:30px;top:242px">Digital Teaching</p>
  <p class="cover-sub" style="left:30px;top:264px;font-size:5px">SUBTITLE GOES HERE</p>
  <span class="year-pill" style="right:18px;bottom:12px;color:#fff;border-color:#fff">2021</span>
</section>

<!-- ===== Row 2 ===== -->
<section class="slide" style="left:27px;top:1565px">
  <svg class="bg" viewBox="0 0 560 314">
    <path d="M300 0 H560 V198 C470 198 390 172 338 112 C312 80 302 40 300 0Z" fill="var(--charcoal)"/>
    <path d="M0 250 C170 250 300 250 420 228 C480 217 530 210 560 206 V198 C470 198 390 172 338 112 C312 80 302 40 300 0 H0Z" fill="var(--orange)"/>
  </svg>
  <div class="ph warm" style="left:0;top:0;width:330px;height:238px;clip-path:path('M0 0 H296 C298 44 310 86 334 118 C360 152 380 170 400 180 C300 228 160 232 0 236 Z')" role="img" aria-label="Graduation cap tassel close-up"></div>
  <h1 class="cover-title" style="left:400px;top:40px">DIGITAL<br>TEACHING<br>MODEL</h1>
  <p class="cover-sub" style="left:400px;top:124px">2021</p>
  <div class="brand" style="left:380px;top:236px"><span class="brand-mark" style="width:16px;height:16px"></span><span class="brand-name" style="font-size:24px">Kestrel</span></div>
  <p class="brand-tag" style="left:404px;top:266px;font-size:5px">LEARN • LEAD • GROW</p>
  <p class="slide-foot" style="font-size:5px">Kestrel™ Vantage Careers™ | 2021 Trademark Kestrel LLC</p>
</section>

<section class="slide" style="left:613px;top:1565px">
  <div class="ph cool" style="inset:0;background:linear-gradient(135deg,#7a6453,#2f2823)" role="img" aria-label="Students smiling while working together in class"></div>
  <svg class="bg" viewBox="0 0 560 314">
    <polygon points="250,0 560,0 560,150" fill="var(--orange)"/>
    <polygon points="340,0 560,0 560,100" fill="#fff"/>
    <polygon points="560,200 560,314 330,314" fill="var(--orange)" opacity=".85"/>
  </svg>
  <div class="brand" style="left:460px;top:26px"><span class="brand-mark" style="width:9px;height:9px"></span><span class="brand-name" style="font-size:14px">Kestrel</span></div>
  <p class="cover-word" style="left:420px;top:262px;color:#fff">Digital Teaching</p>
  <p class="cover-sub" style="left:446px;top:284px;font-size:5px;color:#fff">SUBTITLE GOES HERE</p>
</section>

<!-- ===== Row 3 ===== -->
<section class="slide" style="left:27px;top:1905px">
  <div class="brand" style="left:175px;top:126px"><span class="brand-mark" style="width:26px;height:26px"></span><span class="brand-name" style="font-size:44px">Kestrel</span></div>
  <p class="brand-tag" style="left:212px;top:184px;font-size:8px">LEARN • LEAD • GROW</p>
  <p class="brand-tag" style="left:508px;top:110px;font-size:6px;transform:rotate(90deg);transform-origin:left top">www.kestrel-learning.com</p>
</section>

<section class="slide" style="left:613px;top:1905px">
  <h2 class="slide-title">Evolution of Digital Instructional Tools</h2>
  <svg class="bg" viewBox="0 0 560 314"><line x1="0" y1="180" x2="560" y2="180" stroke="#ccc" stroke-dasharray="2 3"/></svg>
  <div class="era" style="left:40px;top:78px"><div class="era-head o">1985</div><div class="era-shot ph soft" style="position:relative" role="img" aria-label="Early computer lab"></div><div class="era-label">Computer Labs</div></div>
  <div class="era dark" style="left:142px;top:78px"><div class="era-head d">2000</div><div class="era-shot ph soft" style="position:relative" role="img" aria-label="Electronic whiteboard"></div><div class="era-label">Electronic<br>Whiteboards</div></div>
  <div class="era" style="left:244px;top:78px"><div class="era-head o">2010</div><div class="era-shot ph soft" style="position:relative" role="img" aria-label="In-class computing"></div><div class="era-label">In-class Computing</div></div>
  <div class="era dark" style="left:346px;top:78px"><div class="era-head d">2012</div><div class="era-shot ph soft" style="position:relative" role="img" aria-label="Print and digital materials"></div><div class="era-label">Print + Digital</div></div>
  <div class="era" style="left:448px;top:78px"><div class="era-head o">Next Gen</div><div class="era-shot ph soft" style="position:relative" role="img" aria-label="Digital teaching platform classroom"></div><div class="era-label">Digital Teaching<br>Platforms</div></div>
  <p class="slide-foot"><b>6</b>| Kestrel™ Vantage Careers™ 2021 Trademark Kestrel LLC</p><span class="mini-logo"><i></i>Kestrel</span>
</section>

<!-- ===== Row 4 ===== -->
<section class="slide" style="left:27px;top:2245px">
  <svg class="bg" viewBox="0 0 560 314"><polygon points="450,0 560,0 560,80" fill="var(--orange)"/><polygon points="500,0 560,0 560,40" fill="var(--charcoal)"/></svg>
  <p class="copy">The Digital Teaching Platform offers a full curriculum of guided learning sequences with applied activities, media presentations, practice exercises and short quizzes. Before class the teacher uses planning tools to prepare lessons, set goals and choose resources. During class students work alone, in pairs or in groups while the teacher watches progress in real time and adjusts instruction. After class the platform gathers results, builds reports and suggests next steps for every learner. In this way the classroom becomes a flexible space where each student is supported and every teacher stays in control.</p>
  <div class="ph" style="left:305px;top:44px;width:150px;height:226px;background:linear-gradient(135deg,#2e5fae,#17356f)" role="img" aria-label="Book cover on digital teaching platforms"></div>
  <p class="slide-foot"><b>7</b>| Kestrel™ Vantage Careers™ 2021 Trademark Kestrel LLC</p><span class="mini-logo"><i></i>Kestrel</span>
</section>

<section class="slide" style="left:613px;top:2245px">
  <h2 class="slide-title">Traditional LMS Instructional Loop</h2>
  <svg class="bg" viewBox="0 0 560 314">
    <path d="M120 170 A70 70 0 0 1 190 100" fill="none" stroke="var(--orange)" stroke-width="26"/>
    <path d="M190 100 A70 70 0 1 1 120 170" fill="none" stroke="var(--charcoal)" stroke-width="26"/>
    <path d="M284 170 h28 l-7 -8 M312 170 l-7 8" stroke="#aaa" stroke-width="6" fill="none"/>
    <path d="M392 170 h28 l-7 -8 M420 170 l-7 8" stroke="#aaa" stroke-width="6" fill="none"/>
  </svg>
  <div class="loop-box bx-orange" style="left:42px;top:140px;width:80px;height:56px">Content Management</div>
  <div class="loop-box bx-dark" style="left:196px;top:140px;width:80px;height:56px">Assessment</div>
  <div class="loop-box bx-teal" style="left:318px;top:140px;height:56px">Grade Book</div>
  <div class="loop-box bx-purple" style="left:428px;top:140px;height:56px">SIS</div>
  <p class="slide-foot"><b>8</b>| Kestrel™ Vantage Careers™ 2021 Trademark Kestrel LLC</p><span class="mini-logo"><i></i>Kestrel</span>
</section>

<!-- ===== Row 5 ===== -->
<section class="slide" style="left:27px;top:2585px">
  <h2 class="slide-title">Traditional LMS</h2>
  <div class="band">Skinnerian Teaching Machines—ILS's</div>
  <ul class="bullets" style="left:60px;top:130px">
    <li>"Teacher Proof" Technology</li><li>Closed Curriculum</li><li>Fixed Map from Assessment to Curriculum</li><li>Lab or Back of the Room</li><li>One student only</li>
  </ul>
  <div class="ph warm" style="left:400px;top:60px;width:130px;height:254px" role="img" aria-label="Student holding books"></div>
  <p class="slide-foot"><b>9</b>| Kestrel™ Vantage Careers™ 2021 Trademark Kestrel LLC</p><span class="mini-logo"><i></i>Kestrel</span>
</section>

<section class="slide" style="left:613px;top:2585px">
  <h2 class="slide-title">Where is the Locus of Control?</h2>
  <span class="mode-tag">Traditional LMS</span>
  <svg class="locus-lines" viewBox="0 0 560 314"><g stroke="#aaa"><line x1="300" y1="170" x2="280" y2="130"/><line x1="300" y1="170" x2="178" y2="162"/><line x1="300" y1="170" x2="398" y2="166"/><line x1="300" y1="170" x2="280" y2="228"/></g></svg>
  <div class="ph soft ph-teacher" role="img" aria-label="Teacher at classroom board"></div><span class="node-label" style="left:280px;top:118px">Teacher</span>
  <div class="ph soft ph-curric" role="img" aria-label="Curriculum books and worksheets"></div><span class="node-label" style="left:118px;top:193px">Curriculum</span>
  <div class="ph cool ph-tech" role="img" aria-label="Desktop computer"></div><span class="node-label" style="left:437px;top:196px">Technology</span>
  <div class="ph soft ph-student" role="img" aria-label="Students at desks"></div><span class="node-label" style="left:279px;top:268px">Student</span>
  <p class="slide-foot"><b>10</b>| Kestrel™ Vantage Careers™ 2021 Trademark Kestrel LLC</p><span class="mini-logo"><i></i>Kestrel</span>
</section>

<!-- ===== Row 6 ===== -->
<section class="slide" style="left:27px;top:2925px">
  <h2 class="slide-title">Teacher-Centered</h2>
  <span class="mode-tag">Traditional LMS</span>
  <svg class="locus-lines" viewBox="0 0 560 314"><g stroke="#aaa"><line x1="280" y1="160" x2="280" y2="130"/><line x1="280" y1="160" x2="178" y2="162"/><line x1="280" y1="160" x2="398" y2="166"/><line x1="280" y1="160" x2="280" y2="228"/></g><path d="M275 160h10M280 155v10" stroke="var(--charcoal)" stroke-width="1.5"/></svg>
  <div class="ph soft ph-teacher" role="img" aria-label="Teacher at classroom board"></div><span class="node-label" style="left:280px;top:118px">Teacher</span>
  <div class="ph soft ph-curric" role="img" aria-label="Curriculum books and worksheets"></div><span class="node-label" style="left:118px;top:193px">Curriculum</span>
  <div class="ph cool ph-tech" role="img" aria-label="Desktop computer"></div><span class="node-label" style="left:437px;top:196px">Technology</span>
  <div class="ph soft ph-student" role="img" aria-label="Students at desks"></div><span class="node-label" style="left:279px;top:268px">Student</span>
  <p class="slide-foot"><b>11</b>| Kestrel™ Vantage Careers™ 2021 Trademark Kestrel LLC</p><span class="mini-logo"><i></i>Kestrel</span>
</section>

<section class="slide" style="left:613px;top:2925px">
  <h2 class="slide-title">Curriculum-Centered</h2>
  <span class="mode-tag">Traditional LMS</span>
  <svg class="locus-lines" viewBox="0 0 560 314"><g stroke="#aaa"><line x1="220" y1="168" x2="280" y2="130"/><line x1="220" y1="168" x2="178" y2="162"/><line x1="220" y1="168" x2="398" y2="166"/><line x1="220" y1="168" x2="280" y2="228"/></g><path d="M215 168h10M220 163v10" stroke="var(--charcoal)" stroke-width="1.5"/></svg>
  <div class="ph soft ph-teacher" role="img" aria-label="Teacher at classroom board"></div><span class="node-label" style="left:280px;top:118px">Teacher</span>
  <div class="ph soft ph-curric" role="img" aria-label="Curriculum books and worksheets"></div><span class="node-label" style="left:118px;top:193px">Curriculum</span>
  <div class="ph cool ph-tech" role="img" aria-label="Desktop computer"></div><span class="node-label" style="left:437px;top:196px">Technology</span>
  <div class="ph soft ph-student" role="img" aria-label="Students at desks"></div><span class="node-label" style="left:279px;top:268px">Student</span>
  <p class="slide-foot"><b>12</b>| Kestrel™ Vantage Careers™ 2021 Trademark Kestrel LLC</p><span class="mini-logo"><i></i>Kestrel</span>
</section>

<!-- ===== Row 7 ===== -->
<section class="slide" style="left:27px;top:3265px">
  <h2 class="slide-title">Student-Centered</h2>
  <span class="mode-tag">Traditional LMS</span>
  <svg class="locus-lines" viewBox="0 0 560 314"><g stroke="#aaa"><line x1="280" y1="196" x2="280" y2="130"/><line x1="280" y1="196" x2="178" y2="162"/><line x1="280" y1="196" x2="398" y2="166"/><line x1="280" y1="196" x2="280" y2="228"/></g><path d="M275 196h10M280 191v10" stroke="var(--charcoal)" stroke-width="1.5"/></svg>
  <div class="ph soft ph-teacher" role="img" aria-label="Teacher at classroom board"></div><span class="node-label" style="left:280px;top:118px">Teacher</span>
  <div class="ph soft ph-curric" role="img" aria-label="Curriculum books and worksheets"></div><span class="node-label" style="left:118px;top:193px">Curriculum</span>
  <div class="ph cool ph-tech" role="img" aria-label="Desktop computer"></div><span class="node-label" style="left:437px;top:196px">Technology</span>
  <div class="ph soft ph-student" role="img" aria-label="Students at desks"></div><span class="node-label" style="left:279px;top:268px">Student</span>
  <p class="slide-foot"><b>13</b>| Kestrel™ Vantage Careers™ 2021 Trademark Kestrel LLC</p><span class="mini-logo"><i></i>Kestrel</span>
</section>

<section class="slide" style="left:613px;top:3265px">
  <h2 class="slide-title">Technology-Centered</h2>
  <span class="mode-tag">Traditional LMS</span>
  <svg class="locus-lines" viewBox="0 0 560 314"><g stroke="#aaa"><line x1="350" y1="166" x2="280" y2="130"/><line x1="350" y1="166" x2="178" y2="162"/><line x1="350" y1="166" x2="398" y2="166"/><line x1="350" y1="166" x2="280" y2="228"/></g><path d="M345 166h10M350 161v10" stroke="var(--charcoal)" stroke-width="1.5"/></svg>
  <div class="ph soft ph-teacher" role="img" aria-label="Teacher at classroom board"></div><span class="node-label" style="left:280px;top:118px">Teacher</span>
  <div class="ph soft ph-curric" role="img" aria-label="Curriculum books and worksheets"></div><span class="node-label" style="left:118px;top:193px">Curriculum</span>
  <div class="ph cool ph-tech" role="img" aria-label="Desktop computer"></div><span class="node-label" style="left:437px;top:196px">Technology</span>
  <div class="ph soft ph-student" role="img" aria-label="Students at desks"></div><span class="node-label" style="left:279px;top:268px">Student</span>
  <p class="slide-foot"><b>14</b>| Kestrel™ Vantage Careers™ 2021 Trademark Kestrel LLC</p><span class="mini-logo"><i></i>Kestrel</span>
</section>

<!-- ===== Row 8 ===== -->
<section class="slide" style="left:27px;top:3605px">
  <h2 class="slide-title">Digital Teaching Platform-Instructional Loops</h2>
  <svg class="bg" viewBox="0 0 560 314">
    <path d="M130 175 A58 58 0 0 1 188 117" fill="none" stroke="var(--orange)" stroke-width="22"/>
    <path d="M188 117 A58 58 0 1 1 130 175" fill="none" stroke="var(--charcoal)" stroke-width="22"/>
    <path d="M160 81 H70 V125 l-8 -8 M70 125 l8 -8" stroke="#aaa" stroke-width="6" fill="none"/>
    <path d="M280 182 h26 l-7 -7 M306 182 l-7 7" stroke="#aaa" stroke-width="6" fill="none"/>
    <path d="M384 182 h26 l-7 -7 M410 182 l-7 7" stroke="#aaa" stroke-width="6" fill="none"/>
  </svg>
  <div class="loop-box bx-gold" style="left:160px;top:60px;width:70px;height:42px">TEACHER</div>
  <div class="loop-box bx-blue" style="left:34px;top:158px;width:62px;height:48px">Course Syllabus</div>
  <div class="loop-box bx-orange" style="left:120px;top:158px;width:70px;height:50px">Content Management</div>
  <div class="loop-box bx-dark" style="left:204px;top:158px;width:70px;height:50px">Assessment</div>
  <div class="loop-box bx-teal" style="left:312px;top:158px;height:50px">Grade Book</div>
  <div class="loop-box bx-purple" style="left:416px;top:158px;height:50px">SIS</div>
  <p class="slide-foot"><b>15</b>| Kestrel™ Vantage Careers™ 2021 Trademark Kestrel LLC</p><span class="mini-logo"><i></i>Kestrel</span>
</section>

<section class="slide" style="left:613px;top:3605px">
  <h2 class="slide-title">Digital Teaching Platform-Instructional Loops</h2>
  <ul class="bullets" style="left:60px;top:98px">
    <li>Designed for Classroom Use<small>Real Time Classroom Management</small></li>
    <li>Teacher-Centric<small>Scaffolds Teachers</small></li>
    <li>Open Curriculum—Flexible, Teacher-Modifiable</li>
    <li>Lesson Planning Tools</li>
    <li>Individual, Group, and Whole Class Curricula</li>
    <li>Collaborative, Project Centered</li>
    <li>Adaptive Assessment Loop for Personalized Instruction</li>
  </ul>
  <div class="ph warm" style="left:410px;top:70px;width:130px;height:244px" role="img" aria-label="Student holding a notebook"></div>
  <p class="slide-foot"><b>16</b>| Kestrel™ Vantage Careers™ 2021 Trademark Kestrel LLC</p><span class="mini-logo"><i></i>Kestrel</span>
</section>

<!-- ===== Row 9 ===== -->
<section class="slide" style="left:27px;top:3945px">
  <h2 class="slide-title">Where is the Locus of Control?</h2>
  <span class="mode-tag">DT Platform</span>
  <svg class="locus-lines" viewBox="0 0 560 314"><g stroke="#aaa"><line x1="280" y1="168" x2="280" y2="130"/><line x1="280" y1="168" x2="178" y2="162"/><line x1="280" y1="168" x2="398" y2="166"/><line x1="280" y1="168" x2="280" y2="228"/></g><path d="M275 168h10M280 163v10" stroke="var(--charcoal)" stroke-width="1.5"/></svg>
  <div class="ph soft ph-teacher" role="img" aria-label="Teacher at classroom board"></div><span class="node-label" style="left:280px;top:118px">Teacher</span>
  <div class="ph soft ph-curric" role="img" aria-label="Curriculum books and worksheets"></div><span class="node-label" style="left:118px;top:193px">Curriculum</span>
  <div class="ph cool ph-tech" role="img" aria-label="Desktop computer"></div><span class="node-label" style="left:437px;top:196px">Technology</span>
  <div class="ph soft ph-student" role="img" aria-label="Students at desks"></div><span class="node-label" style="left:279px;top:268px">Student</span>
  <p class="slide-foot"><b>17</b>| Kestrel™ Vantage Careers™ 2021 Trademark Kestrel LLC</p><span class="mini-logo"><i></i>Kestrel</span>
</section>

<section class="slide" style="left:613px;top:3945px">
  <h2 class="slide-title">Teacher-Centered</h2>
  <span class="mode-tag">DT Platform</span>
  <svg class="locus-lines" viewBox="0 0 560 314"><g stroke="#aaa"><line x1="280" y1="156" x2="280" y2="130"/><line x1="280" y1="156" x2="178" y2="162"/><line x1="280" y1="156" x2="398" y2="166"/><line x1="280" y1="156" x2="280" y2="228"/></g><path d="M275 156h10M280 151v10" stroke="var(--charcoal)" stroke-width="1.5"/></svg>
  <div class="ph soft ph-teacher" role="img" aria-label="Teacher at classroom board"></div><span class="node-label" style="left:280px;top:118px">Teacher</span>
  <div class="ph soft ph-curric" role="img" aria-label="Curriculum books and worksheets"></div><span class="node-label" style="left:118px;top:193px">Curriculum</span>
  <div class="ph cool ph-tech" role="img" aria-label="Desktop computer"></div><span class="node-label" style="left:437px;top:196px">Technology</span>
  <div class="ph soft ph-student" role="img" aria-label="Students at desks"></div><span class="node-label" style="left:279px;top:268px">Student</span>
  <p class="slide-foot"><b>18</b>| Kestrel™ Vantage Careers™ 2021 Trademark Kestrel LLC</p><span class="mini-logo"><i></i>Kestrel</span>
</section>

<!-- ===== Row 10 ===== -->
<section class="slide" style="left:27px;top:4285px">
  <h2 class="slide-title">Student-Centered</h2>
  <span class="mode-tag">DT Platform</span>
  <svg class="locus-lines" viewBox="0 0 560 314"><g stroke="#aaa"><line x1="280" y1="196" x2="280" y2="130"/><line x1="280" y1="196" x2="178" y2="162"/><line x1="280" y1="196" x2="398" y2="166"/><line x1="280" y1="196" x2="280" y2="228"/></g><path d="M275 196h10M280 191v10" stroke="var(--charcoal)" stroke-width="1.5"/></svg>
  <div class="ph soft ph-teacher" role="img" aria-label="Teacher at classroom board"></div><span class="node-label" style="left:280px;top:118px">Teacher</span>
  <div class="ph soft ph-curric" role="img" aria-label="Curriculum books and worksheets"></div><span class="node-label" style="left:118px;top:193px">Curriculum</span>
  <div class="ph cool ph-tech" role="img" aria-label="Desktop computer"></div><span class="node-label" style="left:437px;top:196px">Technology</span>
  <div class="ph soft ph-student" role="img" aria-label="Students at desks"></div><span class="node-label" style="left:279px;top:268px">Student</span>
  <p class="slide-foot"><b>19</b>| Kestrel™ Vantage Careers™ 2021 Trademark Kestrel LLC</p><span class="mini-logo"><i></i>Kestrel</span>
</section>

<section class="slide" style="left:613px;top:4285px">
  <h2 class="slide-title">Instructional Delivery Scan</h2>
  <table class="scan">
    <tr><th>21st Century School Environment</th><th>Course Platform LMS</th><th>Course Delivery LMS</th><th>Digital Teaching Platform</th><th>Text book</th><th>e-book</th></tr>
    <tr><td>Interactive Digital Environment</td><td><span class="tick">✓</span></td><td><span class="tick">✓</span></td><td><span class="tick">✓</span></td><td></td><td></td></tr>
    <tr><td>Virtual Courses</td><td></td><td><span class="tick">✓</span></td><td></td><td></td><td></td></tr>
    <tr class="gap"><td></td><td></td><td></td><td></td><td></td><td></td></tr>
    <tr><td>Teacher Administration Tools</td><td><span class="tick">✓</span></td><td><span class="tick">✓</span></td><td><span class="tick">✓</span></td><td></td><td></td></tr>
    <tr><td>Student Administration Tools</td><td><span class="tick">✓</span></td><td><span class="tick">✓</span></td><td><span class="tick">✓</span></td><td></td><td></td></tr>
    <tr class="gap"><td></td><td></td><td></td><td></td><td></td><td></td></tr>
    <tr><td>Course Authoring Tools</td><td><span class="tick">✓</span></td><td></td><td><span class="tick">✓</span></td><td></td><td></td></tr>
    <tr><td>Curriculum Content</td><td></td><td><span class="tick">✓</span></td><td><span class="tick">✓</span></td><td><span class="tick">✓</span></td><td><span class="tick">✓</span></td></tr>
    <tr><td>Assessment Content</td><td></td><td><span class="tick">✓</span></td><td><span class="tick">✓</span></td><td><span class="tick">✓</span></td><td><span class="tick">✓</span></td></tr>
    <tr class="gap"><td></td><td></td><td></td><td></td><td></td><td></td></tr>
    <tr><td>Classroom Support</td><td></td><td></td><td><span class="tick">✓</span></td><td></td><td></td></tr>
    <tr><td>Pedagogical Support</td><td></td><td></td><td><span class="tick">✓</span></td><td></td><td></td></tr>
  </table>
  <p class="slide-foot"><b>20</b>| Kestrel™ Vantage Careers™ 2021 Trademark Kestrel LLC</p><span class="mini-logo"><i></i>Kestrel</span>
</section>

</body>
</html>
```